Toy Company Needs a Web Site For a New Toy

We need a web site for a new toy called "Zippa Loop Trike". The bike is a plastic, non motorized ride on toy for kids ages 1.5 - 5 years of age. The bike is being launched in three colors, red, blue and pink, though we may include a black option too.

For the web site we want something bold and colorful that communicates fun, therefore NO dull colors like black or grey. Nothing too cluttered. We want the site to attract the attention of kids but also give the parents a sense of confidence in our professionalism as a trustworthy toy company. The home page should focus on the bike, with different views of the bike and a small write-up on some of its key features. We would also like the home page to have a video of the bike in play. A obvious link to the shopping basket must be present as well. The site must include a shopping basket and ordering system.

Attached is a screenshot of a site that has the colourfulness and playfulness that we are looking for. Please have a look.

The bike images attached are renderings from the CAD software, actual high res photos will be used when the site is developed.

The product logo is attached and MUST be used on the site. It must be BOLD and can be incorporated into the actual website design.

The site pages are:
Home
Gallery
Buy
Contact

Competitors:
www.brambleplay.example
www.quorvaride.example
I do not like either of their sites.

We only have one product at this time, so the site is to be focused on that product, not a whole catalog of products. It is really a single product with the ability to purchase.
Updates

Project Deadline Extended
Reason: I am extending this competition in order to give me more time to review each design and provide the feedback that the designers deserve.

Target Market(s)

Parents, children ages 1.5 - 5.

Industry/Entity Type

It Company

Colors
0555a3
eb1f27
9bcb3c
faed22
f78f20
f37022
e34197
a6459a
6b449b

Requirements
Must have
• Please use the logo attached, but feel free to use different colors.
Should not have
• Dull colors like black and grey

```html
<!DOCTYPE html>
<html lang="en">
<head>
<meta charset="utf-8">
<title>Zippa Loop Trike</title>
<link rel="stylesheet" href="https://fonts.googleapis.com/css2?family=Roboto:wght@400;500;700&family=Roboto+Slab:wght@700&display=swap">
<style>
:root{
  --sky:#36a8dc;
  --red:#e3342f;
  --ink:#1d1d1d;
  --white:#ffffff;
  --rule:#5a5a5a;
  --track:#d4d4d4;
  --player:#2a2a2a;
  --accent:#1ba3e0;
}
*{margin:0;padding:0;box-sizing:border-box}
html,body{width:1200px;height:703px;overflow:hidden;background:var(--white);font-family:"Roboto",Arial,sans-serif}
.page{position:relative;width:1200px;height:703px}

.site-header{position:absolute;left:0;top:0;width:1200px;height:94px;background:var(--white)}
.brand{position:absolute;left:150px;top:27px;display:flex;align-items:center;gap:10px}
.brand-dot{width:40px;height:40px;border-radius:50%;background:var(--red)}
.brand-name{font-family:"Roboto Slab",Georgia,serif;font-weight:700;font-size:20px;color:var(--red);white-space:nowrap}

.main-nav{position:absolute;left:643px;top:24px;width:341px;display:flex;justify-content:space-between;padding:0 0 5px 14px;border-bottom:1px solid var(--rule)}
.main-nav a{font-weight:500;font-size:15px;color:var(--ink);text-decoration:none;white-space:nowrap}
.sub-nav{position:absolute;right:216px;top:58px;display:flex;align-items:center;gap:9px;font-size:12px;color:var(--ink);white-space:nowrap}
.sub-nav .sep{color:#777}
.social{display:flex;gap:3px}
.social span{width:13px;height:13px;background:var(--ink)}
.cart{position:absolute;left:1003px;top:26px;width:47px;height:47px;border:1px solid var(--rule)}
.cart svg{position:absolute;left:11px;top:12px}
.cart-count{position:absolute;right:4px;top:-7px;width:15px;height:15px;border-radius:50%;background:var(--red);color:var(--white);font-size:9px;font-weight:700;display:flex;align-items:center;justify-content:center}

.hero{position:absolute;left:0;top:94px;width:1200px;height:590px;background:var(--sky)}
.tagline{position:absolute;left:0;top:62px;width:1200px;text-align:center;font-family:"Roboto Slab",Georgia,serif;font-weight:700;font-size:40px;line-height:48px;color:var(--white)}

.video{position:absolute;left:150px;top:130px;width:574px;height:323px;background:linear-gradient(180deg,#4f6b3a 0%,#6f8f45 45%,#3f43b8 60%,#2f2f9a 80%,#2c2c2c 100%)}
.video-actions{position:absolute;right:10px;top:9px;display:flex;flex-direction:column;gap:5px}
.video-action{width:44px;height:36px;background:rgba(30,30,30,.85);border-radius:3px;color:var(--white);font-size:9px;font-weight:700;display:flex;flex-direction:column;align-items:center;justify-content:center;gap:2px}
.video-controls{position:absolute;left:15px;bottom:11px;width:545px;height:30px;display:flex;gap:8px}
.play{width:53px;height:30px;background:rgba(30,30,30,.9);border-radius:3px;display:flex;align-items:center;justify-content:center}
.scrub{flex:1;background:rgba(30,30,30,.9);border-radius:3px;position:relative}
.scrub-track{position:absolute;left:10px;top:12px;width:372px;height:6px;background:#555}
.scrub-fill{position:absolute;left:0;top:0;width:113px;height:6px;background:var(--accent)}
.scrub-time{position:absolute;left:108px;top:-9px;background:#111;color:var(--white);font-size:8px;padding:1px 3px}
.scrub-meta{position:absolute;right:10px;top:8px;display:flex;gap:6px;align-items:center;color:var(--accent);font-size:10px;font-weight:700;font-style:italic}

.pitch{position:absolute;left:742px;top:136px;width:310px;display:flex;flex-direction:column;align-items:flex-start}
.intro{font-size:14px;line-height:20.6px;letter-spacing:-.1px;color:var(--white)}
.order-btn{margin-top:20px;width:219px;height:56px;background:var(--red);border-radius:6px;color:var(--white);font-family:"Roboto Slab",Georgia,serif;font-weight:700;font-size:20px;display:flex;align-items:center;justify-content:center;gap:10px;text-decoration:none;white-space:nowrap}

.scroll-bike{position:absolute;left:150px;top:525px;width:99px;height:65px;background:linear-gradient(180deg,#b9b9b9,#4a4a4a);border-radius:30px 30px 8px 8px}
.footer-track{position:absolute;left:0;top:684px;width:1200px;height:19px;background:var(--white)}
.footer-track .progress{width:249px;height:19px;background:var(--track)}
</style>
</head>
<body>
<div class="page">
  <header class="site-header">
    <div class="brand"><span class="brand-dot"></span><span class="brand-name">Zippa Loop Trike</span></div>
    <nav class="main-nav">
      <a href="#">HOME</a><a href="#">GALLERY</a><a href="#">ORDER NOW</a><a href="#">CONTACT</a>
    </nav>
    <div class="sub-nav">
      <span>About</span><span class="sep">/</span><span>Shipping</span><span class="sep">/</span><span>Return</span><span class="sep">/</span>
      <span class="social"><span></span><span></span><span></span></span>
    </div>
    <a class="cart" href="#" aria-label="Shopping basket">
      <svg width="25" height="22" viewBox="0 0 25 22"><path d="M7 8 L12.5 1 L18 8" fill="none" stroke="#1d1d1d" stroke-width="2"/><rect x="0" y="7" width="25" height="4" fill="#1d1d1d"/><path d="M2 12 H23 L21 22 H4 Z" fill="#1d1d1d"/></svg>
      <span class="cart-count">1</span>
    </a>
  </header>

  <section class="hero">
    <h1 class="tagline">Tagline Goes Here</h1>

    <div class="video" role="img" aria-label="Video still of a blue ride-on toy motorbike on a park path">
      <div class="video-actions">
        <div class="video-action"><svg width="16" height="13" viewBox="0 0 16 13"><path d="M8 13 L1 6 A3.5 3.5 0 0 1 8 2 A3.5 3.5 0 0 1 15 6 Z" fill="#fff"/></svg>LIKE</div>
        <div class="video-action"><svg width="14" height="12" viewBox="0 0 14 12"><path d="M2 10 L11 2 M7 2 H11 V6" fill="none" stroke="#fff" stroke-width="2"/></svg>SHARE</div>
        <div class="video-action"><svg width="18" height="12" viewBox="0 0 18 12"><path d="M5 2 L1 6 L5 10 M13 2 L17 6 L13 10 M10 1 L8 11" fill="none" stroke="#fff" stroke-width="2"/></svg>EMBED</div>
      </div>
      <div class="video-controls">
        <div class="play"><svg width="12" height="13" viewBox="0 0 12 13"><path d="M0 0 L12 6.5 L0 13 Z" fill="#fff"/></svg></div>
        <div class="scrub">
          <div class="scrub-track"><div class="scrub-fill"></div></div>
          <span class="scrub-time">00:34</span>
          <div class="scrub-meta"><span>IIIIIII</span><span>HD</span>
            <svg width="10" height="10" viewBox="0 0 10 10"><path d="M0 3 V0 H3 M7 0 H10 V3 M10 7 V10 H7 M3 10 H0 V7" fill="none" stroke="#fff" stroke-width="1.5"/></svg>
          </div>
        </div>
      </div>
    </div>

    <div class="pitch">
      <p class="intro">Lorem ipsum dolor sit amet, consectetur adipiscing elit. In ut cursus orci. Suspendisse porttitor laoreet erat non luctus. Aliquam fermentum eros vitae accumsan vulputate. Aliquam erat volutpat. Quisque eu nibh nisl. Pellentesque tempus neque vitae nunc tincidunt pharetra. Quisque dapibus tortor ac libero convallis, ac posuere erat lacinia. Phasellus tempor massa non sagittis fringilla. Aenean faucibus pulvinar orci sed aliquet. Pellentesque hendrerit lacinia fringilla onec sagittis risus ac.</p>
      <a class="order-btn" href="#"><span>★</span><span>ORDER NOW!</span><span>★</span></a>
    </div>

    <div class="scroll-bike" role="img" aria-label="Small silver toy motorbike marking scroll progress"></div>
  </section>

  <div class="footer-track"><div class="progress"></div></div>
</div>
</body>
</html>
```